Venue Booking Site

I would like a venue directory and booking website designed. The idea is that end users will come to the site to find venues for weddings, parties, events etc. They will be able to find the venue based on many criteria, the most important ones are availability and location - they will be able to see in real time which venues are available for the desired dates and areas.

Venues will be able to use the website as a reservation management tool, receive payments for bookings through the site and be able to manage bookings on the go. This will be made into an app. It needs to be developed in bootstrap. Brand name to be used: Mirqona. Venue, place and space bookings.

Target audience - end users - anyone who is looking for a venue. For Community members it will provide an easy way to find a suitable venue
Outline what dates and times the venue is available
Outline costs involved in booking the venue
Search via many other criteria
It will allow the customer to book and pay for the venue online in one smooth process

Clients: Venue managers - particularly focussing on not for profit businesses eg, GHAs, community hall managers, small business managers. These people typically use paper based systems yet and do not use websites so it needs to be very user friendly. Future growth to restaurants, pubs, event venues who have a stronger familiarity with computers and who might already use their own booking management tool - so this needs to be able to link in with their system.

What need will this meet for venue managers:
This tool provides venues with greater visibility, promotion and advertising of their venue
This allows more customers to find them and book with them
This tool will be offered to not-for-profit venue managers for free to better connect them to the community
This means greater profit for these community venues
This means more revenue and jobs created in these communities

Sample of the layout / contents attached. This is not a complete site map as yet as it is a work in progress for final pages.

Small Business

5+ page

Sans Serif

eb2027

• This is a psd file only - one template for each different section, home page, search page, detailed page view, admin back end
• does not need to be coded.
• Note, the golden lantern logo jpeg files were files we were toying with using for this project- but I am happy to use the main mirqona logo- I will let you decide.

```html
<!DOCTYPE html>
<html lang="en">
<head>
<meta charset="utf-8">
<title>Mirqona – Venue, place and space bookings</title>
<link href="https://fonts.googleapis.com/css2?family=Open+Sans:wght@400;600;700&family=PT+Serif:wght@400;700&family=Lato:wght@400;700&display=swap" rel="stylesheet">
<style>
:root{
  --brand:#eb2027;
  --brand-dark:#a5171c;
  --brand-deep:#7d1014;
  --ink:#333;
  --muted:#777;
  --line:#d9d9d9;
  --panel:#f2f2f2;
  --page:#e9e9e9;
  --white:#fff;
  --nav-dark:#2b2b2b;
  --map-base:#e8e4dc;
  --map-park:#cfe3b3;
  --star:#f0a020;
  --star-off:#c8c8c8;
}
*{box-sizing:border-box;margin:0;padding:0}
html,body{width:800px;height:1200px;overflow:hidden}
body{position:relative;background:var(--page);font-family:"Open Sans",Arial,sans-serif;color:var(--ink);font-size:9px}
.serif{font-family:"PT Serif",Georgia,serif}

/* Top bar */
.topbar{position:absolute;left:0;top:0;width:800px;height:33px;background:linear-gradient(#b01c22,var(--brand-deep))}
.topbar .icons{position:absolute;left:122px;top:6px;display:flex;gap:12px}
.topbar .support{position:absolute;left:333px;top:7px;color:var(--white);font-weight:700;font-size:14px;display:flex;align-items:center;gap:6px}
.topbar .btns{position:absolute;left:543px;top:7px;display:flex;gap:6px}
.top-btn{background:linear-gradient(#fafafa,#cfcfcf);border:1px solid #888;border-radius:2px;font-size:9px;padding:2px 10px;color:#222}

/* Header */
.header{position:absolute;left:0;top:33px;width:800px;height:87px;background:linear-gradient(#fdfdfd,#e4e4e4);border-bottom:1px solid #ccc}
.brand{position:absolute;left:118px;top:18px;display:flex;align-items:center;gap:8px}
.brand .mark{width:26px;height:26px;background:var(--brand);border-radius:50%}
.brand .name{font-family:"Lato",sans-serif;font-weight:700;font-size:34px;color:var(--brand);letter-spacing:-.5px}
.login{position:absolute;left:301px;top:9px;display:flex;align-items:center;gap:5px;font-size:10px;font-weight:600}
.field{height:18px;border:1px solid #bbb;background:var(--white);font-size:8px;color:#999;padding:3px 4px}
.go{background:var(--brand);color:var(--white);font-weight:700;font-size:8px;height:18px;padding:3px 4px}
.sitesearch{position:absolute;left:544px;top:9px;width:139px;height:18px;border:1px solid #bbb;border-radius:3px;background:var(--white);font-size:8px;color:#999;padding:3px 5px}
.nav{position:absolute;left:265px;top:43px;height:28px;display:flex;background:linear-gradient(#f7f7f7,#d9d9d9);border:1px solid #bbb;border-radius:3px;box-shadow:0 2px 3px rgba(0,0,0,.15)}
.nav a{display:block;padding:0 9px;line-height:26px;font-size:9px;color:#333;text-decoration:none;border-right:1px solid #c4c4c4}
.nav a:last-child{border-right:0}
.nav a.active{background:var(--nav-dark);color:var(--white);font-weight:700;border-radius:3px 0 0 3px}

/* Map */
.map{position:absolute;left:0;top:120px;width:800px;height:296px;background:linear-gradient(160deg,var(--map-base),#ddd8ce 60%,var(--map-park) 75%,var(--map-base))}

/* Search */
.search{position:absolute;left:0;top:416px;width:800px;height:124px;background:linear-gradient(#fafafa,#ececec);border-top:1px solid #ccc}
.search .col{position:absolute;top:0;height:108px;border-right:1px solid var(--line)}
.search h3{font-family:"PT Serif",Georgia,serif;font-size:12px;color:var(--brand-dark);text-align:center;padding-top:8px;height:30px;border-bottom:1px solid var(--line)}
.search .body{padding:7px 8px 0;font-family:"PT Serif",Georgia,serif;font-size:8.5px;color:#444}
.opt{display:flex;align-items:center;gap:5px;margin-bottom:4px}
.chk{width:8px;height:8px;border:1px solid #999;background:var(--white)}
.chk.on{background:var(--brand);border-color:var(--brand)}
.inp{margin-top:6px;height:17px;border:1px solid #bbb;background:var(--white);font-size:7.5px;color:#999;padding:3px 4px;display:flex;justify-content:space-between;align-items:center}
.dates{display:flex;gap:6px}
.dates>div{flex:1}
.search-btn{position:absolute;left:357px;top:104px;width:86px;height:18px;background:linear-gradient(#e5262d,var(--brand-dark));color:var(--white);font-weight:700;font-size:10px;text-align:center;line-height:18px;border-radius:8px 8px 0 0}

/* Top venues band */
.band{position:absolute;left:0;top:540px;width:800px;height:31px;background:linear-gradient(#3a3a3a,#1e1e1e)}
.band .tab{position:absolute;left:0;top:0;height:31px;width:270px;background:linear-gradient(#e2252c,var(--brand-deep));clip-path:polygon(0 0,250px 0,270px 31px,0 31px)}
.band h2{position:absolute;left:125px;top:5px;color:var(--white);font-family:"Lato",sans-serif;font-size:15px;font-weight:700}

/* Venue cards */
.venues{position:absolute;left:0;top:571px;width:800px;height:265px;background:#efefef;border-bottom:1px solid #ccc}
.card{position:absolute;top:16px;width:126px;height:242px;background:var(--white);box-shadow:0 1px 3px rgba(0,0,0,.2);padding:4px}
.card .photo{position:relative;height:107px}
.card .photo span{position:absolute;left:0;bottom:0;right:0;background:rgba(0,0,0,.6);color:var(--white);font-family:"PT Serif",Georgia,serif;font-weight:700;font-size:9px;padding:2px 4px}
.card .meta{display:flex;justify-content:space-between;font-size:8.5px;color:#555;padding:7px 2px 5px;border-bottom:1px solid #ddd}
.card p{font-size:7.5px;color:#888;line-height:1.35;padding:5px 2px 0;height:50px}
.card .rate{display:flex;justify-content:space-between;align-items:center;padding:0 2px;font-size:7.5px;color:var(--brand)}
.card .price-label{font-size:7.5px;font-weight:700;color:#333;padding:6px 2px 2px}
.card .buy{display:flex;justify-content:space-between;align-items:center;padding:0 2px}
.card .amt{color:var(--brand);font-size:12px;font-weight:700}
.book{background:#1c1c1c;color:var(--white);font-size:8.5px;padding:3px 7px;border-radius:2px}
.p1{background:linear-gradient(#6e7f95,#3c4350 55%,#c9c7c2)}
.p2{background:linear-gradient(#4c6ea0,#2f9ab7 55%,#5a4c3a)}
.p3{background:linear-gradient(#2c3556,#5a4c66 45%,#8c6a45)}
.p4{background:linear-gradient(#8fb0cc,#3c6f8d 55%,#2a3540)}

/* Why */
.why{position:absolute;left:0;top:837px;width:800px;height:240px;background:#ececec}
.why h2{text-align:center;font-family:"Lato",sans-serif;font-weight:400;font-size:16px;color:#444;padding-top:8px}
.feat{position:absolute;width:132px;height:87px;background:var(--white);border:1px solid #ddd;box-shadow:0 1px 2px rgba(0,0,0,.08);padding:7px}
.feat h4{font-family:"PT Serif",Georgia,serif;color:var(--brand-dark);font-size:9px;font-weight:400;padding-bottom:5px;border-bottom:1px solid #e2e2e2}
.feat p{font-size:7.5px;color:#888;line-height:1.35;padding-top:5px}

/* Footer */
.footer{position:absolute;left:0;top:1077px;width:800px;height:123px;background:var(--white)}
.fcol{position:absolute;top:8px;font-size:8px;color:#444}
.fbrand{display:flex;align-items:center;gap:5px;font-size:10px;font-weight:700;margin-bottom:8px}
.fbrand .tag{background:#888;color:var(--white);padding:1px 4px;border-radius:2px;font-weight:700}
.fcol li{list-style:none;display:flex;align-items:center;gap:6px;margin-bottom:6px}
.fcol h5{font-family:"PT Serif",Georgia,serif;font-size:9.5px;font-weight:400;margin-bottom:6px}
.fcol .links li{margin-bottom:4px}
.social{display:flex;gap:5px;margin:8px 0 10px}
.social i{display:block;width:16px;height:16px;border-radius:50%;background:var(--brand)}
.news{display:flex;align-items:center;gap:6px}
.news .field{width:125px}
.signup{background:var(--brand-dark);color:var(--white);font-size:7.5px;font-weight:700;padding:4px 7px}
.bottom{position:absolute;left:117px;top:100px;width:566px;border-top:1px solid #ddd;padding-top:6px;display:flex;justify-content:space-between;font-size:7.5px;color:#555}
.bottom nav{display:flex}
.bottom nav a{color:#555;text-decoration:none;padding:0 7px;border-left:1px solid #ccc}
.bottom nav a:first-child{border-left:0}
</style>
</head>
<body>

<header class="topbar">
  <div class="icons">
    <svg width="16" height="16" viewBox="0 0 16 16"><circle cx="6.5" cy="6.5" r="4.5" fill="none" stroke="#fff" stroke-width="2"/><line x1="10" y1="10" x2="14.5" y2="14.5" stroke="#fff" stroke-width="2.5"/></svg>
    <svg width="16" height="16" viewBox="0 0 16 16"><rect x="1.5" y="2.5" width="13" height="12" fill="none" stroke="#fff" stroke-width="1.5"/><rect x="1.5" y="2.5" width="13" height="3" fill="#fff"/><g fill="#fff"><rect x="4" y="8" width="2" height="2"/><rect x="7" y="8" width="2" height="2"/><rect x="10" y="8" width="2" height="2"/><rect x="4" y="11" width="2" height="2"/><rect x="7" y="11" width="2" height="2"/></g></svg>
    <svg width="17" height="16" viewBox="0 0 17 16"><path d="M1 8 8.5 1.5 16 8" fill="none" stroke="#fff" stroke-width="2"/><path d="M3.5 7v8h4v-4h2v4h4V7" fill="#fff"/></svg>
  </div>
  <div class="support">
    <svg width="18" height="18" viewBox="0 0 18 18"><circle cx="9" cy="9" r="8" fill="#fff"/><path d="M5.5 5.5c1-1 2-.5 2.3.6l-.8 1c.5 1.3 1.4 2.2 2.7 2.7l1-.8c1.1.3 1.6 1.3.6 2.3-1.8 1.8-7.6-4-5.8-5.8z" fill="var(--brand-dark)"/></svg>
    <span>24/7 Support &nbsp;03 5550 1427</span>
  </div>
  <div class="btns"><span class="top-btn">Home</span><span class="top-btn">List My Venue</span></div>
</header>

<div class="header">
  <div class="brand"><span class="mark"></span><span class="name">mirqona</span></div>
  <div class="login">Login: <span class="field" style="width:88px">Username</span><span class="field" style="width:84px">Password</span><span class="go">GO</span></div>
  <div class="sitesearch">Search entire Site here</div>
  <nav class="nav">
    <a class="active">HOME</a><a>VENUE</a><a>NEWS &amp; OFFERS</a><a>INSPIRATION</a><a>SERVICES</a><a>CONTACT</a><a>FAQs</a>
  </nav>
</div>

<div class="map" role="img" aria-label="Street map of the surrounding suburb with a pin on the venue address"></div>

<section class="search">
  <div class="col" style="left:120px;width:127px">
    <h3>What?</h3>
    <div class="body">
      <div class="opt"><span class="chk on"></span>Hotel</div>
      <div class="opt"><span class="chk"></span>Rent a Car</div>
      <div class="opt"><span class="chk"></span>Self Catering</div>
      <div class="opt"><span class="chk"></span>Tour</div>
    </div>
  </div>
  <div class="col" style="left:247px;width:150px">
    <h3>Where</h3>
    <div class="body">Your Desination<div class="inp">City, Region, District or specific</div></div>
  </div>
  <div class="col" style="left:397px;width:152px">
    <h3>When?</h3>
    <div class="body"><div class="dates">
      <div>Check in Date<div class="inp">11/12/2014 <span>▦</span></div></div>
      <div>Check-out Date<div class="inp">15/12/2014 <span>▦</span></div></div>
    </div></div>
  </div>
  <div class="col" style="left:549px;width:134px;border-right:0">
    <h3>Who?</h3>
    <div class="body">Rooms<div class="inp" style="width:60px">2 Rooms <span>⬍</span></div></div>
  </div>
  <div class="search-btn">SEARCH</div>
</section>

<div class="band"><div class="tab"></div><h2>Our Top Venues</h2></div>

<section class="venues">
  <article class="card" style="left:117px">
    <div class="photo p1" role="img" aria-label="Modern house with a covered outdoor lounge at dusk"><span>PRIME APPARTMENT</span></div>
    <div class="meta"><span>Ut wisi enim</span><span>8/10</span></div>
    <p>Lorem ipsum dolor sit amet, consectetuer adipiscing elit, sed diam nonummy nibh euismod.</p>
    <div class="rate"><svg width="40" height="8" viewBox="0 0 40 8"><g><path id="s" d="M4 0l1.2 2.6 2.8.3-2.1 1.9.6 2.8L4 6.2 1.5 7.6l.6-2.8L0 2.9l2.8-.3z" fill="var(--star)"/><use href="#s" x="10"/><use href="#s" x="20"/><use href="#s" x="30" fill="var(--star-off)"/></g></svg><span>More Info</span></div>
    <div class="price-label">Price per room per night from</div>
    <div class="buy"><span class="amt">$80</span><span class="book">Book Now</span></div>
  </article>
  <article class="card" style="left:264px">
    <div class="photo p2" role="img" aria-label="Resort swimming pool lit at twilight"><span>TROPICANA PALMS</span></div>
    <div class="meta"><span>Ut wisi enim</span><span>8/10</span></div>
    <p>Lorem ipsum dolor sit amet, consectetuer adipiscing elit, sed diam nonummy nibh euismod.</p>
    <div class="rate"><svg width="40" height="8" viewBox="0 0 40 8"><use href="#s" fill="var(--star)"/><use href="#s" x="10"/><use href="#s" x="20"/><use href="#s" x="30" fill="var(--star-off)"/></svg><span>More Info</span></div>
    <div class="price-label">Price per room per night from</div>
    <div class="buy"><span class="amt">$80</span><span class="book">Book Now</span></div>
  </article>
  <article class="card" style="left:411px">
    <div class="photo p3" role="img" aria-label="Villa garden path with palm trees in evening light"><span>VILLA IPSUM</span></div>
    <div class="meta"><span>Ut wisi enim</span><span>8/10</span></div>
    <p>Lorem ipsum dolor sit amet, consectetuer adipiscing elit, sed diam nonummy nibh euismod.</p>
    <div class="rate"><svg width="40" height="8" viewBox="0 0 40 8"><use href="#s"/><use href="#s" x="10"/><use href="#s" x="20"/><use href="#s" x="30" fill="var(--star-off)"/></svg><span>More Info</span></div>
    <div class="price-label">Price per room per night from</div>
    <div class="buy"><span class="amt">$80</span><span class="book">Book Now</span></div>
  </article>
  <article class="card" style="left:557px">
    <div class="photo p4" role="img" aria-label="Modern glass apartment with a pool deck under blue sky"><span>PRIME APPARTMENT</span></div>
    <div class="meta"><span>Ut wisi enim</span><span>8/10</span></div>
    <p>Lorem ipsum dolor sit amet, consectetuer adipiscing elit, sed diam nonummy nibh euismod.</p>
    <div class="rate"><svg width="40" height="8" viewBox="0 0 40 8"><use href="#s"/><use href="#s" x="10"/><use href="#s" x="20"/><use href="#s" x="30" fill="var(--star-off)"/></svg><span>More Info</span></div>
    <div class="price-label">Price per room per night from</div>
    <div class="buy"><span class="amt">$80</span><span class="book">Book Now</span></div>
  </article>
</section>

<section class="why">
  <h2>Why should you book your venue through Mirqona?</h2>
  <div class="feat" style="left:114px;top:39px"><h4>Handpicked Hotels</h4><p>Lorem ipsum dolor sit amet, consectetuer adipiscing elit, sed diam nonummy consectetuer adipiscing elit, nibh euismod.</p></div>
  <div class="feat" style="left:261px;top:39px"><h4>Detailed Descriptions</h4><p>Lorem ipsum dolor sit amet, consectetuer adipiscing elit, sed diam nonummy consectetuer adipiscing elit, nibh euismod.</p></div>
  <div class="feat" style="left:408px;top:39px"><h4>Exclusive Knowledge</h4><p>Lorem ipsum dolor sit amet, consectetuer adipiscing elit, sed diam nonummy consectetuer adipiscing elit, nibh euismod.</p></div>
  <div class="feat" style="left:554px;top:39px"><h4>Passionate Service</h4><p>Lorem ipsum dolor sit amet, consectetuer adipiscing elit, sed diam nonummy consectetuer adipiscing elit, nibh euismod.</p></div>
  <div class="feat" style="left:114px;top:140px"><h4>Best Price Guarantee</h4><p>Lorem ipsum dolor sit amet, consectetuer adipiscing elit, sed diam nonummy consectetuer adipiscing elit, nibh euismod.</p></div>
  <div class="feat" style="left:261px;top:140px"><h4>Secure Booking</h4><p>Lorem ipsum dolor sit amet, consectetuer adipiscing elit, sed diam nonummy consectetuer adipiscing elit, nibh euismod.</p></div>
  <div class="feat" style="left:408px;top:140px"><h4>Benefits for Hotellers</h4><p>Lorem ipsum dolor sit amet, consectetuer adipiscing elit, sed diam nonummy consectetuer adipiscing elit, nibh euismod.</p></div>
  <div class="feat" style="left:554px;top:140px"><h4>Any Questions ?</h4><p>Lorem ipsum dolor sit amet, consectetuer adipiscing elit, sed diam nonummy consectetuer adipiscing elit, nibh euismod.</p></div>
</section>

<footer class="footer">
  <div class="fcol" style="left:117px">
    <div class="fbrand"><span class="tag">mirqona</span> Bookings</div>
    <ul>
      <li><svg width="7" height="10" viewBox="0 0 7 10"><path d="M3.5 0A3.5 3.5 0 0 0 0 3.5C0 6 3.5 10 3.5 10S7 6 7 3.5A3.5 3.5 0 0 0 3.5 0z" fill="#555"/><circle cx="3.5" cy="3.5" r="1.3" fill="#fff"/></svg>12 Alder Crt Linwood VIC.</li>
      <li><svg width="7" height="10" viewBox="0 0 7 10"><rect x="1" y="0" width="5" height="10" rx="1" fill="#555"/></svg>03 5550 1428</li>
      <li><svg width="9" height="7" viewBox="0 0 9 7"><rect width="9" height="7" fill="#555"/><path d="M0 0l4.5 4L9 0" fill="none" stroke="#fff"/></svg>info@bookings.mirqona.com.au</li>
    </ul>
  </div>
  <div class="fcol" style="left:261px">
    <h5>Customer Support</h5>
    <ul class="links">
      <li>• FAQs</li><li>• How do i make a reservation?</li><li>• Payment options</li><li>• Booking tips</li>
    </ul>
  </div>
  <div class="fcol" style="left:408px">
    <h5>Follow us</h5>
    <div class="social"><i></i><i></i><i></i><i></i><i></i><i></i><i></i><i></i></div>
    <div class="news"><h5 style="margin:0">Our exclusive offers</h5><span class="field">Enter your email here</span><span class="signup">SIGNUP</span></div>
  </div>
  <div class="bottom">
    <span>© 2014, mirqona.com. &nbsp;All Rights Reserved.</span>
    <nav><a>HOME</a><a>VENUE</a><a>NEWS &amp; OFFERS</a><a>INSPIRATION</a><a>SERVICES</a><a>CONTACT</a><a>FAQs</a></nav>
  </div>
</footer>

</body>
</html>
```